Stationery Set for new venture capital firm

We need a new set of stationery including letterhead, business cards, envelopes, with compliment slips for our new startup venture capital firm known as Halvora.
We make alternative investments globally and hope to have a worldwide network of offices later.

The stationery should be elegant and not too fussy with the use of too many colors.

Venture Capital

```html
<!DOCTYPE html>
<html lang="en">
<head>
<meta charset="utf-8">
<title>Halvora Stationery Set</title>
<link rel="stylesheet" href="https://fonts.googleapis.com/css2?family=Open+Sans:wght@400;600;700&display=swap">
<style>
  :root {
    --bg: #ececec;
    --paper: #ffffff;
    --brand-blue: #4aa0d6;
    --brand-grey: #6e6e6e;
    --text: #8a8a8a;
    --rule: #d6d6d6;
    --shadow: rgba(0,0,0,0.08);
  }
  * { box-sizing: border-box; margin: 0; padding: 0; }
  html, body { width: 1200px; height: 1000px; overflow: hidden; }
  body {
    background: var(--bg);
    font-family: "Open Sans", Arial, sans-serif;
    color: var(--text);
    position: relative;
  }
  .sheet {
    position: absolute;
    background: var(--paper);
    box-shadow: 0 2px 10px var(--shadow);
    overflow: hidden;
  }
  .wordmark {
    display: flex; align-items: center; gap: 6px;
    color: var(--brand-grey); font-weight: 700; letter-spacing: -0.2px;
  }
  .wordmark .dot { border-radius: 50%; background: var(--brand-blue); flex: none; }
  .corner-disc { position: absolute; border-radius: 50%; background: var(--brand-blue); }
  .contact-block { position: absolute; color: #fff; line-height: 1.55; white-space: nowrap; }
  .contact-block .org { font-weight: 700; }

  /* business card front */
  .card-front { left: 60px; top: 60px; width: 300px; height: 172px;
    display: flex; align-items: center; justify-content: center; }
  .card-front .wordmark { font-size: 26px; }
  .card-front .dot { width: 14px; height: 14px; }

  /* business card back */
  .card-back { left: 380px; top: 60px; width: 300px; height: 172px; }
  .card-back .wordmark { position: absolute; left: 20px; top: 18px; font-size: 11px; }
  .card-back .dot { width: 7px; height: 7px; }
  .card-back .person { position: absolute; left: 20px; top: 70px; }
  .card-back .person-name { color: var(--brand-blue); font-size: 15px; font-weight: 400; }
  .card-back .person-role { font-size: 8px; color: var(--text); }
  .card-back .corner-disc { width: 230px; height: 230px; left: 150px; top: 60px; }
  .card-back .contact-block { left: 200px; top: 104px; font-size: 6px; }

  /* compliment slip */
  .slip { left: 60px; top: 262px; width: 620px; height: 290px; }
  .slip .wordmark { position: absolute; left: 40px; top: 60px; font-size: 30px; }
  .slip .dot { width: 16px; height: 16px; }

  /* envelope */
  .envelope { left: 60px; top: 582px; width: 620px; height: 310px; }
  .envelope .flap-line { position: absolute; left: 0; right: 0; top: 44px; height: 1px; background: #eeeeee; }
  .envelope .sender { position: absolute; right: 40px; bottom: 34px; width: 130px; }
  .envelope .wordmark { font-size: 15px; }
  .envelope .dot { width: 9px; height: 9px; }
  .envelope .sender-lines { margin-top: 6px; font-size: 6.5px; line-height: 1.6; color: var(--text); white-space: nowrap; }
  .envelope .sender-lines .org { color: var(--brand-blue); font-weight: 600; }
  .envelope .sender-lines svg { width: 6px; height: 6px; vertical-align: -1px; margin-right: 3px; }

  /* letterhead */
  .letterhead { left: 710px; top: 60px; width: 440px; height: 832px; }
  .letterhead .wordmark { position: absolute; left: 0; right: 0; top: 44px; justify-content: center; font-size: 26px; }
  .letterhead .dot { width: 13px; height: 13px; }
  .letter-meta { position: absolute; left: 26px; top: 142px; width: 84px; font-size: 7.5px; line-height: 1.25; }
  .letter-meta dt { color: var(--brand-blue); font-weight: 700; text-transform: uppercase; }
  .letter-meta dd { margin-bottom: 7px; }
  .letter-divider { position: absolute; left: 116px; top: 142px; width: 1px; height: 300px; background: var(--rule); }
  .letter-body { position: absolute; left: 132px; top: 142px; width: 282px; font-size: 7px; line-height: 1.65; }
  .letter-title { font-size: 10px; color: var(--brand-grey); margin-bottom: 14px; white-space: nowrap; }
  .letter-title strong { color: var(--brand-blue); font-weight: 700; }
  .letter-body p { margin-bottom: 11px; }
  .sign-off { position: absolute; right: 44px; top: 520px; width: 110px; text-align: center; font-size: 8px; }
  .signature { margin-top: 8px; width: 110px; height: 34px; background: linear-gradient(90deg, #e3e3e3, #cfcfcf); border-radius: 3px; }
  .letterhead .corner-disc { width: 320px; height: 320px; left: 210px; top: 660px; }
  .letterhead .contact-block { left: 292px; top: 702px; font-size: 7px; }
</style>
</head>
<body>
  <section class="sheet card-front" aria-label="Business card front">
    <div class="wordmark"><span class="dot"></span>Halvora</div>
  </section>

  <section class="sheet card-back" aria-label="Business card back">
    <div class="wordmark"><span class="dot"></span>Halvora</div>
    <div class="person">
      <div class="person-name">Marek Olsen</div>
      <div class="person-role">Managing Director</div>
    </div>
    <div class="corner-disc"></div>
    <div class="contact-block">
      <div class="org">Halvora Venture Capital</div>
      <div>24 Harbour Lane, London</div>
      <div>+44 20 7946 0182</div>
      <div>marek@halvora.com</div>
    </div>
  </section>

  <section class="sheet slip" aria-label="Compliment slip">
    <div class="wordmark"><span class="dot"></span>Halvora</div>
  </section>

  <section class="sheet envelope" aria-label="Envelope">
    <div class="flap-line"></div>
    <div class="sender">
      <div class="wordmark"><span class="dot"></span>Halvora</div>
      <div class="sender-lines">
        <div class="org">Halvora Venture Capital</div>
        <div><svg viewBox="0 0 10 10"><path d="M5 0C3 0 1.5 1.5 1.5 3.5 1.5 6 5 10 5 10s3.5-4 3.5-6.5C8.5 1.5 7 0 5 0z" fill="#4aa0d6"/></svg>24 Harbour Lane, London</div>
        <div><svg viewBox="0 0 10 10"><path d="M2 0h2l1 3-1.5 1a6 6 0 0 0 2.5 2.5L7 5l3 1v2a2 2 0 0 1-2 2C4 10 0 6 0 2a2 2 0 0 1 2-2z" fill="#4aa0d6"/></svg>+44 20 7946 0182</div>
        <div><svg viewBox="0 0 10 10"><rect x="0" y="2" width="10" height="6" fill="#4aa0d6"/></svg>info@halvora.com</div>
      </div>
    </div>
  </section>

  <section class="sheet letterhead" aria-label="Letterhead">
    <div class="wordmark"><span class="dot"></span>Halvora</div>
    <dl class="letter-meta">
      <dt>Subject</dt><dd>Lorem ipsum</dd>
      <dt>Date</dt><dd>03.01.2014</dd>
      <dt>Adressed to</dt><dd>Elin Varga</dd>
    </dl>
    <div class="letter-divider"></div>
    <div class="letter-body">
      <div class="letter-title"><strong>Nulla sodales:</strong> Lorem ipsum dolor sit amet.</div>
      <p>Dear Client,</p>
      <p>Thank you for meeting with our team last week. We were glad to learn more about your plans and the market you hope to reach. Our partners have reviewed the material you shared and would like to continue the conversation in the coming weeks.</p>
      <p>We invest in early companies across several regions and support founders with capital, advice and access to our network. Please find enclosed a short summary of our terms and the next steps we propose. We look forward to hearing from you soon.</p>
      <p>Best regards,</p>
    </div>
    <div class="sign-off">
      <div>Director</div>
      <div class="signature" role="img" aria-label="Handwritten signature of Marek Olsen"></div>
    </div>
    <div class="corner-disc"></div>
    <div class="contact-block">
      <div class="org">Halvora Venture Capital</div>
      <div>24 Harbour Lane</div>
      <div>London, United Kingdom</div>
      <div>+44 20 7946 0182</div>
      <div>info@halvora.com</div>
      <div>www.halvora.com</div>
    </div>
  </section>
</body>
</html>
```